" A Quitavel é uma empresa que desenvolve e fornece o sistema de cobrança Quitavel para empresas de cobrança (escritórios de cobrança, assessorias de cobranças, escritórios de advogados), tais clientes chamamos de ASSESSORIAS, e também fornecemos o sistema para empresas que possuem uma grande quantidade de clientes inadimplentes e que fazem a cobrança destes clientes internamente através de um departamento de cobrança, estes clientes chamamos de CREDORES. Alguns clientes ASSESSORIAS: www.grupoltn-exemplo.com.br www.moraisetavares-exemplo.com.br www.rvrecupera-exemplo.com.br Alguns clientes CREDORES: www.linguaviva-exemplo.com www.grupovelarium-exemplo.com.br www.ronaldos-exemplo.com.br Todos os produtos e serviços que comercializamos são através da plataforma Quitavel, por exemplo, para que um cliente utilize nosso produto “Portal de Negociação” ele precisa contratar o Quitavel já que suas configurações são através do sistema, da mesma forma o serviço de “SMS”, já que as campanhas são criadas e disparadas pelo sistema Quitavel. O sistema Quitavel “nasceu” primeiro que a empresa Quitavel, já que dois dos atuais sócios possuíram uma empresa anterior de 2012 até a abertura da Quitavel em 1 de setembro de 2015. Esta empresa desenvolvia um sistema focado para assessorias de cobrança, porém em uma tecnologia antiga, e então resolveram criar um novo software com tecnologias atuais na época e para isto buscaram um investidor e juntos optaram por criar uma nova empresa, uma nova marca. Nossa logo foi construída através da plataforma Marca Pronta e gostamos muito do resultado! E estamos aqui novamente buscando que seus profissionais nos ajudem a criar novos materiais que hoje se fazem necessários para nós. "

```html
<!DOCTYPE html>
<html lang="pt-BR">
<head>
<meta charset="utf-8">
<title>Plataforma de Cobrança — Quitavel</title>
<link rel="stylesheet" href="https://fonts.googleapis.com/css2?family=Open+Sans:wght@400;600;700&display=swap">
<style>
  :root{
    --page-bg:#e9ebef;
    --slide-bg:#ffffff;
    --brand-blue:#2255a4;
    --brand-navy:#1d3876;
    --strip-blue:#2f5fb3;
    --text:#4a4f57;
    --photo-light:#d7dde6;
    --photo-dark:#6f7c8f;
    --diagram-light:#e3f1f8;
    --diagram-mid:#bcd9ec;
  }
  *{box-sizing:border-box;margin:0;padding:0}
  html,body{width:1200px;height:1200px;overflow:hidden}
  body{background:var(--page-bg);font-family:"Open Sans",Arial,sans-serif;position:relative}
  .slide{position:absolute;left:40px;top:285px;width:1120px;height:630px;background:var(--slide-bg);overflow:hidden;box-shadow:0 2px 10px rgba(0,0,0,.08)}
  .slide-title{position:absolute;left:78px;top:48px;font-size:28px;font-weight:700;color:var(--brand-blue);letter-spacing:-.2px}
  .title-rule{position:absolute;left:78px;top:92px;width:270px;border-top:2px dotted var(--brand-blue)}
  .brand{position:absolute;right:38px;top:28px;display:flex;align-items:center;gap:8px}
  .brand-mark{width:16px;height:16px;border-radius:50%;background:var(--brand-blue)}
  .brand-name{font-size:24px;font-weight:700;color:var(--brand-blue)}
  .body-copy{position:absolute;left:78px;top:128px;width:790px;color:var(--text);font-size:12.6px;line-height:1.62}
  .body-copy p{margin-bottom:17px;text-align:justify}
  .infra-diagram{position:absolute;left:620px;top:478px;width:250px;height:100px;border-radius:6px;background:linear-gradient(90deg,var(--diagram-light) 0%,var(--diagram-mid) 50%,var(--diagram-light) 100%)}
  .side-strip{position:absolute;left:895px;top:120px;width:42px;height:486px;background:var(--strip-blue)}
  .side-photo{position:absolute;left:937px;top:80px;width:183px;height:526px;background:linear-gradient(160deg,var(--photo-light) 0%,#aeb8c6 55%,var(--photo-dark) 100%)}
  .footer-band{position:absolute;left:0;bottom:0;width:100%;height:24px;background:var(--brand-navy)}
</style>
</head>
<body>
  <section class="slide">
    <h1 class="slide-title">Plataforma de Cobrança</h1>
    <div class="title-rule"></div>

    <div class="brand">
      <span class="brand-mark"></span>
      <span class="brand-name">Quitavel</span>
    </div>

    <div class="body-copy">
      <p>A Quitavel inova ao oferecer uma plataforma de cobrança única e comercializada no modelo SaaS, software como serviço, no qual somos responsáveis pela estrutura necessária para disponibilização dos softwares, incluindo servidores de hospedagem e tudo o que envolve a segurança das informações.</p>
      <p>Ao contratar Quitavel sua empresa tem acesso ao sistema de cobrança que mais cresce no mercado e a vários produtos e serviços conectados à plataforma, como SMS, E-mail, Localização Cadastral, Discador, Portal de Negociação, Canais de Negociação através de Chatbot, ZapLine e Falaí Messenger. Todos fornecidos através de parceiros estratégicos integrados à nossa plataforma, o que faz dela a única que atua com este modelo de negócio.</p>
      <p>A plataforma também integra Credores e Assessorias gerando oportunidade de negócios para ambos! Já que a empresa credora pode contratar e distribuir sua carteira de inadimplentes a qualquer uma das assessorias que utilizam o Quitavel e as Assessorias podem prestar serviços a qualquer um dos Credores que utilizam Quitavel.</p>
      <p>Para garantir a qualidade dos nossos serviços quanto a desempenho, segurança e disponibilidade, em 2018 migramos toda a nossa infraestrutura para o Celesta da Nubora e nos juntamos a 90% das empresas da Lista Prime 500 que trabalham com o Nubora Cloud a qual oferece a maior cobertura de conformidade que nenhum outro provedor de nuvem oferece.</p>
    </div>

    <div class="infra-diagram" role="img" aria-label="Ilustração de infraestrutura em nuvem com ícones de segurança conectados"></div>

    <div class="side-strip"></div>
    <div class="side-photo" role="img" aria-label="Fotografia de atendente com headset em central de cobrança"></div>
    <div class="footer-band"></div>
  </section>
</body>
</html>
```